Creative Flyer Design Project

I want to create a flyer. I have attached wireframe (wireframe.png) of flyer which gives you much needed idea regarding flyer content. I have attached few images from our portfolio which can be used while designing a flyer.

I would like you to show me the extreme creativity and capability in delivering world class flyer design.

No heavy graphics needed. I want extremely clean and professional flyer using icons, colors and highlighted text/headings.

I will be requiring multiple formats of flyer such as .ai/.png/.psd/pdf.

Size of flyer: Standard A4 size OR Height is at discretion of designer. The width must be below 780 px.

Fonts to be used: Web 2.0 fonts needed. Must drive message clearly.

*** Long term association oppurtunity exists for the right creative designers for direct work

Target Market(s)

Business owners

Industry/Entity Type

Work

Requirements
Should not have
• Cartoonish or cheap graphics

```html
<!DOCTYPE html>
<html lang="en">
<head>
<meta charset="utf-8">
<title>Graphic Print Website Design – Flyer</title>
<link rel="stylesheet" href="https://fonts.googleapis.com/css2?family=Source+Sans+3:wght@400;600;700&display=swap">
<style>
  :root{
    --paper:#ffffff;
    --sheet-light:#e2e6e9;
    --sheet-dark:#c3ccd3;
    --brown:#3a2120;
    --magenta:#e5007d;
    --sky:#29a8e0;
    --lemon:#fff35a;
    --headline:#e3e3e3;
    --white:#ffffff;
    --brand-grey:#5d5f63;
  }
  *{box-sizing:border-box;margin:0;padding:0}
  html,body{width:867px;height:1200px;overflow:hidden;background:var(--paper)}
  body{font-family:"Source Sans 3",Arial,sans-serif;color:var(--brown)}

  .canvas{position:relative;width:650px;height:900px;transform:scale(1.3338,1.3334);transform-origin:0 0}

  .sheet{
    position:absolute;left:35px;top:33px;width:580px;height:833px;overflow:hidden;
    background:linear-gradient(110deg,var(--sheet-light) 0%,#d3d9de 55%,var(--sheet-dark) 100%);
  }

  /* brand lockups */
  .brand{position:absolute;left:448px;display:flex;align-items:center;gap:7px}
  .brand--company{top:31px}
  .brand--sponsor{top:67px}
  .brand__mark{width:28px;height:24px;flex:none}
  .brand--company .brand__mark{background:var(--magenta)}
  .brand--sponsor .brand__mark{background:var(--sky);border-radius:50%;width:24px}
  .brand__name{font-size:10.5px;line-height:10px;font-weight:600;color:var(--brand-grey);letter-spacing:.4px;text-transform:uppercase}

  /* tilted composition */
  .stage{position:absolute;left:175px;top:145px;width:0;height:0;transform:rotate(-31deg);transform-origin:0 0}

  .band{
    position:absolute;height:58px;display:flex;align-items:center;padding-left:9px;
    font-size:64px;font-weight:700;line-height:1;letter-spacing:-2.5px;color:var(--headline);
    background:var(--brown);box-shadow:3px 3px 0 rgba(0,0,0,.22);
    text-shadow:2px 2px 0 rgba(0,0,0,.45);white-space:nowrap;
  }
  .band--graphic{left:-118px;top:-31px;width:304px}
  .band--print{left:-118px;top:37px;width:253px}
  .band--website{left:-95px;top:105px;width:265px}
  .band--design{left:-106px;top:173px;width:215px;background:var(--magenta)}

  .price-ribbon{
    position:absolute;left:-122px;top:-140px;width:380px;height:38px;
    transform:rotate(90deg);transform-origin:0 0;background:var(--sky);
    display:flex;align-items:center;padding-left:62px;
    font-size:25.5px;font-weight:700;letter-spacing:-1px;color:var(--white);white-space:nowrap;
  }

  .services{position:absolute;left:-104px;top:248px;white-space:nowrap}
  .services__title{font-size:16px;font-weight:600;line-height:20px}
  .services__note{font-size:14px;line-height:20px;color:var(--white);padding-left:6px;margin-top:4px}
  .services__list{list-style:none;margin-top:44px;padding-left:6px;font-size:12.5px;font-weight:600;line-height:16px}
  .services__list .cont{padding-left:22px}

  .contact{
    position:absolute;left:-124px;top:263px;width:470px;
    transform:rotate(90deg);transform-origin:0 0;white-space:nowrap;
  }
  .offer{font-size:16px;font-weight:600;line-height:18px}
  .offer .soft{color:var(--white);font-weight:400}
  .site{
    margin:13px 0 0 -10px;width:258px;height:38px;background:var(--lemon);
    display:flex;align-items:center;padding-left:16px;
    font-size:30px;font-weight:700;letter-spacing:-.5px;color:var(--white);
    text-shadow:1px 1px 0 rgba(0,0,0,.12);
  }
  .call{margin-top:8px;font-size:15px;font-weight:700;line-height:20px;padding-left:14px}
  .process{margin-top:10px;padding-left:8px}
  .process__title{font-size:14px;font-weight:700;line-height:16px}
  .process__list{list-style:none;font-size:14px;line-height:15.6px}

  .guarantee-badge{position:absolute;left:390px;top:547px;width:140px;height:140px;transform:rotate(-14deg)}
</style>
</head>
<body>
<div class="canvas">
  <main class="sheet">

    <div class="brand brand--company">
      <span class="brand__mark"></span>
      <span class="brand__name">Your<br>Company</span>
    </div>
    <div class="brand brand--sponsor">
      <span class="brand__mark"></span>
      <span class="brand__name">Sponsor<br>Name</span>
    </div>

    <div class="stage">
      <div class="price-ribbon">MOST AFFORDABLE PRICE!</div>

      <h1 class="band band--graphic">GRAPHIC</h1>
      <div class="band band--print">PRINT</div>
      <div class="band band--website">WEBSITE</div>
      <div class="band band--design">DESIGN</div>

      <section class="services">
        <p class="services__title">Our Services are available in 36 categories</p>
        <p class="services__note">Don't forget to check Our Portfolio</p>
        <ul class="services__list">
          <li>01 Creatively Crafted Functional Designs</li>
          <li>02 Highly Affordable Pricing</li>
          <li>03 Multiple Variations of Designs Submitted</li>
          <li>04 Variations open to Revisions</li>
          <li>05 Guaranteed 48 hours Delievery</li>
          <li>06 30,000+ ready Designs avaiable all open for</li>
          <li class="cont">customizaion at NO extra cost</li>
        </ul>
      </section>

      <section class="contact">
        <p class="offer">21% Special Discount <span class="soft">to Studio Circle members Use:</span> flyer2013</p>
        <p class="site">www.yourfolio.com</p>
        <p class="call">Call us now: 555-24680-1357</p>
        <div class="process">
          <h2 class="process__title">Our Design Process</h2>
          <ol class="process__list">
            <li>01. Carefull analysis of need</li>
            <li>02. creation of rough hand drawn sketches</li>
            <li>03. Analysing sketches and shortlisting them</li>
            <li>04. Conversion of sketches into Digital Formats</li>
            <li>05. Submission of multiple Designs to Choose from</li>
            <li>06. Feedback rounds to give final shape to Design</li>
            <li>07.Delever of Design in different formats.</li>
          </ol>
        </div>
      </section>
    </div>

    <svg class="guarantee-badge" viewBox="0 0 140 140" role="img" aria-label="Satisfaction guarantee seal">
      <circle cx="70" cy="70" r="64" fill="none" stroke="var(--brown)" stroke-width="3"/>
      <circle cx="70" cy="70" r="58" fill="none" stroke="var(--brown)" stroke-width="1.5"/>
      <circle cx="70" cy="70" r="40" fill="none" stroke="var(--brown)" stroke-width="2"/>
    </svg>

  </main>
</div>
</body>
</html>
```